Granola stand up bag packaging. Full Bleed printed on the bag. Full Color.

I Have a design I made but we are about to order thousands of printed bags so I thought I'd get a real designer to do the design. We do however want some sort of window area so the customer can see the granola through the bag. I have Illustrator native files of the logo for anyone who would like them. We have 3 flavors, so this is the first and we also have a coffee flavor, and a Oh Yeah flavor that we will need packaging for. The sample file is the package I designed myself, and like, however if we are going to pull the trigger on a $4,000 bag order then I want a design to use for the next 10 years!!

Target Market(s)

Granola Loving People at Natural Food Stores like Fernway Pantry.

Font styles to use
Sans Serif

Colors
acd036
ffffff
fbee3e

Requirements
Must have
• My logo, Some sort of transparent area so the customer can see the beautiful granola in the bag. Nutritional Facts and Bar Code area. Weight on the front of the bag.

```html
<!DOCTYPE html>
<html lang="en">
<head>
<meta charset="utf-8">
<title>Cedar Hill Granola Company – Original</title>
<link rel="stylesheet" href="https://fonts.googleapis.com/css2?family=Alfa+Slab+One&family=Oswald:wght@600&family=Raleway:wght@300;400&display=swap">
<style>
  :root {
    --page: #f1f1f1;
    --sun: #fbc02d;
    --lemon: #fbee3e;
    --tangerine: #f59a1f;
    --flame: #e8461e;
    --ember: #d9381a;
    --forest: #1f4a22;
    --forest-mid: #2f6b2c;
    --lime: #acd036;
    --ink: #16301a;
    --white: #ffffff;
    --ribbon: #e2581f;
    --ribbon-dark: #b33c12;
  }
  html, body {
    margin: 0;
    width: 899px;
    height: 1200px;
    overflow: hidden;
    background: var(--page);
  }
  .canvas {
    position: relative;
    width: 899px;
    height: 1200px;
  }
  .bag-art {
    position: absolute;
    inset: 0;
  }
  .brand-name {
    position: absolute;
    left: 275px;
    top: 206px;
    width: 348px;
    text-align: center;
    font-family: "Oswald", sans-serif;
    font-weight: 600;
    font-size: 40px;
    line-height: 1.05;
    letter-spacing: 1px;
    color: var(--ink);
    text-transform: uppercase;
    margin: 0;
  }
  .flavor-name {
    font-family: "Alfa Slab One", serif;
    font-size: 56px;
    fill: var(--white);
    letter-spacing: 2px;
  }
  .tagline {
    position: absolute;
    left: 92px;
    width: 715px;
    top: 1004px;
    margin: 0;
    text-align: center;
    font-family: "Raleway", sans-serif;
    font-weight: 300;
    font-size: 19px;
    line-height: 29px;
    color: var(--white);
  }
  .net-weight {
    position: absolute;
    left: 92px;
    width: 715px;
    top: 1094px;
    margin: 0;
    text-align: center;
    font-family: "Raleway", sans-serif;
    font-weight: 400;
    font-size: 26px;
    color: var(--lemon);
  }
</style>
</head>
<body>
<main class="canvas">
  <svg class="bag-art" width="899" height="1200" viewBox="0 0 899 1200" xmlns="http://www.w3.org/2000/svg">
    <defs>
      <clipPath id="bag-shape">
        <rect x="92" y="40" width="715" height="1120" rx="14"/>
      </clipPath>
      <linearGradient id="flame-fill" x1="0" y1="0" x2="1" y2="1">
        <stop offset="0" stop-color="#f06a22"/>
        <stop offset="1" stop-color="#e23a1a"/>
      </linearGradient>
      <radialGradient id="granola-tones" cx="0.5" cy="0.5" r="0.6">
        <stop offset="0" stop-color="#c9a57c"/>
        <stop offset="0.6" stop-color="#a27a52"/>
        <stop offset="1" stop-color="#6e4a2c"/>
      </radialGradient>
    </defs>

    <g class="bag-body" clip-path="url(#bag-shape)">
      <rect class="bag-base" x="92" y="40" width="715" height="1120" fill="var(--sun)"/>
      <polygon class="stripe-flame" points="500,40 807,40 807,760 640,500" fill="url(#flame-fill)"/>
      <polygon class="stripe-orange" points="92,40 500,40 640,500 807,760 807,900 92,420" fill="var(--tangerine)" opacity="0.55"/>
      <polygon class="stripe-lemon" points="92,300 92,520 807,980 807,820" fill="var(--lemon)" opacity="0.7"/>
      <polygon class="stripe-ember" points="92,620 92,989 807,989 807,900" fill="var(--ember)" opacity="0.55"/>

      <g class="center-band">
        <rect x="322" y="40" width="254" height="950" fill="var(--forest)"/>
        <rect x="346" y="40" width="10" height="950" fill="var(--forest-mid)"/>
        <rect x="542" y="40" width="10" height="950" fill="var(--forest-mid)"/>
        <rect x="372" y="40" width="154" height="950" fill="var(--forest-mid)"/>
      </g>

      <rect class="footer-band" x="92" y="989" width="715" height="171" fill="var(--forest)"/>
      <rect class="footer-rule" x="92" y="980" width="715" height="4" fill="var(--tangerine)"/>
    </g>

    <circle class="brand-seal" cx="449" cy="266" r="174" fill="var(--lime)"/>

    <g class="flavor-ribbon">
      <polygon points="158,850 230,820 250,940 172,930 196,890" fill="var(--ribbon-dark)"/>
      <polygon points="740,850 668,820 648,940 726,930 702,890" fill="var(--ribbon-dark)"/>
      <path d="M210,860 Q449,790 688,860 L688,972 Q449,902 210,972 Z" fill="var(--ribbon)"/>
    </g>

    <circle class="window-rim" cx="449" cy="689" r="210" fill="var(--white)"/>
    <circle class="granola-window" cx="449" cy="689" r="202" fill="url(#granola-tones)" role="img" aria-label="Photo of toasted oat granola with pecans, dried cranberries and apricot pieces"/>

    <path class="ribbon-front" d="M236,905 Q449,842 662,905 L662,985 Q449,922 236,985 Z" fill="var(--ribbon)"/>
    <path id="flavor-curve" d="M250,962 Q449,902 648,962" fill="none"/>
    <text class="flavor-name" text-anchor="middle"><textPath href="#flavor-curve" startOffset="50%">ORIGINAL</textPath></text>
  </svg>

  <p class="brand-name">Cedar Hill<br>Granola<br>Company</p>

  <p class="tagline">Good granola will sustain and energize you.<br>Great granola will do that and taste delicious as well.<br>Cedar Hill Granola Company is handmade, great granola!</p>
  <p class="net-weight">net wt 12 oz (340 g)</p>
</main>
</body>
</html>
```